Coastal Bright Sweep Business Card

We are a cleaning and waste management company with the slogan "making waste to landfill a thing of the past". We would like a re-design of our current business card. On the front we want to continue to use our logo as the focus point. On the back, we want the whole thing re-done to be less busy. We want the staff member’s name, the job title, mobile number, email and website. We do not want the address on the card. We still want the green, black and blue colours used, but a new font for the information on the back. Please do not change the logo design at all. We are also thinking about using icons to replace the text ‘mobile, email, website’. The “events + commercial” banner needs to be incorporated somewhere and needs to read “events + commercial + waste”. Another important point for consideration is that we are very concerned about being environmentally sustainable and will be printing on recycled paper. All designs should be made to compliment this in regards to boldness and colouring. Please find attached our logo, our colour chart and an image of our current business card.

```html
<!DOCTYPE html>
<html lang="en">
<head>
<meta charset="utf-8">
<title>Coastal Bright Sweep Business Card</title>
<link rel="stylesheet" href="https://fonts.googleapis.com/css2?family=Roboto:wght@400;700;900&family=Roboto+Condensed:wght@400;700&display=swap">
<style>
  :root {
    --navy: #0f3f73;
    --leaf: #7dc242;
    --sky: #16aee8;
    --paper: #f3f3f2;
    --white: #ffffff;
    --backdrop: #e7e4df;
  }
  * { margin: 0; padding: 0; box-sizing: border-box; }
  html, body { width: 1200px; height: 960px; overflow: hidden; }
  body { background: var(--backdrop); position: relative; font-family: "Roboto", Arial, sans-serif; }

  .card {
    position: absolute;
    width: 600px;
    height: 343px;
    border-radius: 22px;
    overflow: hidden;
    box-shadow: 0 3px 8px rgba(0,0,0,0.25);
  }
  .card-front { left: 314px; top: 113px; background: var(--paper); }
  .card-back { left: 312px; top: 473px; background: var(--navy); }

  .front-shapes { position: absolute; inset: 0; }

  .contact-block { position: absolute; left: 25px; top: 108px; color: var(--white); }
  .staff-name {
    font-family: "Roboto Condensed", Arial, sans-serif;
    font-weight: 700; font-size: 21px; letter-spacing: 0.2px; line-height: 1;
  }
  .staff-role {
    font-family: "Roboto Condensed", Arial, sans-serif;
    font-weight: 400; font-size: 15px; margin-top: 7px; letter-spacing: 0.3px;
  }
  .contact-list { list-style: none; margin-top: 23px; }
  .contact-list li { display: flex; align-items: center; font-size: 14px; height: 19.5px; }
  .contact-list svg { width: 12px; height: 12px; margin-right: 8px; flex: none; }

  .brand-front {
    position: absolute; left: 360px; top: 108px; width: 220px;
    text-align: center; color: var(--navy);
    font-weight: 900; font-size: 36px; line-height: 40px;
  }

  .brand-back {
    position: absolute; left: 0; right: 0; top: 88px;
    text-align: center; color: var(--white);
    font-weight: 900; font-size: 44px; line-height: 48px;
  }
  .service-banner {
    position: absolute; left: 158px; top: 278px; width: 283px; height: 30px;
    background: var(--white); border-radius: 5px;
    color: var(--navy); font-weight: 700; font-size: 16px;
    display: flex; align-items: center; justify-content: center; letter-spacing: 0.2px;
  }
</style>
</head>
<body>

<section class="card card-front">
  <svg class="front-shapes" viewBox="0 0 600 343" width="600" height="343">
    <path d="M276 0 H300 C372 95 368 250 290 343 H272 C348 250 350 95 276 0 Z" fill="var(--leaf)"/>
    <path d="M270 0 H278 C352 95 350 250 276 343 H268 C342 250 344 95 270 0 Z" fill="var(--sky)"/>
    <path d="M0 0 H268 C340 95 338 250 266 343 H0 Z" fill="var(--navy)"/>
  </svg>

  <div class="contact-block">
    <h1 class="staff-name">MORGAN ELLERY</h1>
    <p class="staff-role">CLIENT MANAGER</p>
    <ul class="contact-list">
      <li>
        <svg viewBox="0 0 12 12"><rect x="2.5" y="0.5" width="7" height="11" rx="1.2" fill="none" stroke="var(--white)" stroke-width="1.4"/><rect x="5" y="9" width="2" height="1" fill="var(--white)"/></svg>
        0400 555 218
      </li>
      <li>
        <svg viewBox="0 0 12 12"><rect x="0.5" y="2.5" width="11" height="7.5" fill="var(--white)"/><path d="M0.5 2.5 L6 7 L11.5 2.5" fill="none" stroke="var(--navy)" stroke-width="1"/></svg>
        mellery@coastalbrightsweep.com.au
      </li>
      <li>
        <svg viewBox="0 0 12 12"><circle cx="6" cy="6" r="5.5" fill="var(--white)"/><path d="M3 3.5 Q5 5 4 7 Q6 8 5.5 10.5 M8 2.5 Q7.5 5 9.5 6" fill="none" stroke="var(--navy)" stroke-width="1"/></svg>
        www.coastalbrightsweep.com.au
      </li>
    </ul>
  </div>

  <div class="brand-front">Coastal<br>Bright<br>Sweep</div>
</section>

<section class="card card-back">
  <div class="brand-back">Harbour<br>Bright Sweep</div>
  <div class="service-banner">EVENTS, COMMERCIAL &amp; WASTE</div>
</section>

</body>
</html>
```